New Television Homescreen Template

We need a new default homescreen design for our televisions. This should reflect our company branding. My company is called Wellward Systems, WSY for short. Our website is www.wsyq.com. We develop televisions and infotainment solutions for the healthcare industry. I am somewhat open to different color palettes but our company colors are blue, black, and white. Our design is constrained by the 9 buttons, however the design of the buttons can be changed. Also, there is a video box on the right side of the screen as shown, this design can also be changed.

Target Market(s)

Hospital Patients

Requirements
Must have
• PSD template.

```html
<!DOCTYPE html>
<html lang="en">
<head>
<meta charset="utf-8">
<title>Wellward Systems – Homescreen</title>
<link rel="stylesheet" href="https://fonts.googleapis.com/css2?family=Open+Sans:wdth,wght@75..100,400..700&display=swap">
<style>
  :root {
    --bg-deep: #4a5566;
    --bg-mid: #8e9bb2;
    --bg-glow: #e8eef8;
    --bg-warm: #e9b8c4;
    --btn-top: #4b8fd6;
    --btn-bottom: #2a67b4;
    --btn-edge: #1b4488;
    --btn-label: #2b5b93;
    --btn-label-shadow: rgba(255, 255, 255, 0.35);
    --frame-dark: #05072a;
    --frame-navy: #1c2585;
    --frame-lip: #7d82c2;
    --frame-band: #8a8fc8;
    --brand-ink: #1d2833;
  }

  * { margin: 0; padding: 0; box-sizing: border-box; }

  html, body {
    width: 1200px;
    height: 675px;
    overflow: hidden;
    background: var(--bg-deep);
  }

  .homescreen {
    position: relative;
    width: 1200px;
    height: 675px;
    overflow: hidden;
    font-family: "Open Sans", Arial, sans-serif;
  }

  .homescreen__backdrop {
    position: absolute;
    inset: 0;
    background:
      radial-gradient(ellipse 260px 150px at 740px 470px, rgba(255,255,255,0.85), rgba(255,255,255,0) 70%),
      radial-gradient(circle 150px at 1080px 300px, var(--bg-warm), rgba(233,184,196,0) 70%),
      radial-gradient(ellipse 520px 420px at 800px 300px, var(--bg-glow), rgba(232,238,248,0) 75%),
      linear-gradient(180deg, var(--bg-mid) 0%, #7d8aa4 45%, var(--bg-deep) 100%);
  }

  .channel-grid {
    position: absolute;
    left: 54px;
    top: 63px;
    display: grid;
    grid-template-columns: 239px 239px;
    grid-auto-rows: 97px;
    column-gap: 65px;
    row-gap: 47px;
  }

  .channel-button {
    display: flex;
    align-items: center;
    justify-content: center;
    border-radius: 6px;
    background: linear-gradient(180deg, var(--btn-top) 0%, var(--btn-bottom) 100%);
    border-bottom: 7px solid var(--btn-edge);
    box-shadow: 0 2px 4px rgba(0, 0, 0, 0.35), inset 0 1px 0 rgba(255,255,255,0.35);
    color: var(--btn-label);
    font-size: 48px;
    font-weight: 600;
    font-stretch: 75%;
    letter-spacing: 0.5px;
    text-shadow: 1px 1px 0 var(--btn-label-shadow), -1px -1px 0 rgba(10, 40, 90, 0.45);
    padding-top: 4px;
    white-space: nowrap;
  }

  .video-frame {
    position: absolute;
    left: 648px;
    top: 206px;
    width: 494px;
    height: 238px;
  }

  .brand {
    position: absolute;
    right: 44px;
    top: 40px;
    display: flex;
    align-items: center;
    gap: 10px;
    color: var(--brand-ink);
    font-size: 34px;
    font-weight: 400;
    font-stretch: 88%;
    line-height: 1;
    white-space: nowrap;
  }

  .brand__mark {
    width: 14px;
    height: 14px;
    background: var(--brand-ink);
  }
</style>
</head>
<body>
  <main class="homescreen">
    <div class="homescreen__backdrop" role="img" aria-label="Starry space background with a bright light burst"></div>

    <nav class="channel-grid" aria-label="Channels">
      <div class="channel-button">CABLE TV</div>
      <div class="channel-button">CABLE TV</div>
      <div class="channel-button">CABLE TV</div>
      <div class="channel-button">CABLE TV</div>
      <div class="channel-button">CABLE TV</div>
      <div class="channel-button">CABLE TV</div>
      <div class="channel-button">CABLE TV</div>
      <div class="channel-button">CABLE TV</div>
    </nav>

    <svg class="video-frame" viewBox="0 0 494 238" aria-label="Video window">
      <path fill="var(--frame-dark)" fill-rule="evenodd"
            d="M5 0 H489 Q494 0 494 5 V233 Q494 238 489 238 H5 Q0 238 0 233 V5 Q0 0 5 0 Z
               M13 11 V213 H481 V11 Z"/>
      <path fill="var(--frame-navy)" d="M4 2 H490 L481 11 H13 Z"/>
      <path fill="var(--frame-navy)" d="M4 2 L13 11 V213 L4 222 Z"/>
      <path fill="var(--frame-navy)" d="M490 2 L481 11 V213 L490 222 Z"/>
      <path fill="var(--frame-lip)" d="M5 0 H489 L486 3 H8 Z"/>
      <rect x="13" y="11" width="468" height="4" fill="var(--frame-dark)"/>
      <path fill="var(--frame-band)" d="M13 190 H481 V213 H13 Z"/>
      <path fill="#a3a7d8" d="M13 190 H481 L476 193 H18 Z"/>
    </svg>

    <div class="brand"><span class="brand__mark"></span>Wellward Systems</div>
  </main>
</body>
</html>
```